Lena Marwick Biz Card
biz card and stationary
Lena Marwick Biz Card - Financial Services
Creative Brief
Bright & Fun-filled
Lena Marwick
Independent Agent
Charlotte, NC
Lenamarwick@quillpost.example
www.marwickInsurance.example
Please use the head shot attached and the logo.
I will be uploading an example of content for the back of their card. please use that information.

```html
<!DOCTYPE html>
<html lang="en">
<head>
<meta charset="utf-8">
<title>Lena Marwick Business Card</title>
<link rel="stylesheet" href="https://fonts.googleapis.com/css2?family=Tinos:wght@400;700&display=swap">
<style>
  :root{
    --stage:#7b7b7b;
    --stage-edge:#3f3f3f;
    --navy:#0d2a7a;
    --navy-deep:#071a57;
    --royal:#1f46b3;
    --green:#4cae3f;
    --green-light:#9fd13c;
    --green-deep:#3a9a3c;
    --ink:#111111;
    --paper:#ffffff;
  }
  *{box-sizing:border-box;margin:0;padding:0}
  html,body{width:1200px;height:713px;overflow:hidden}
  body{
    background:var(--stage);
    border:14px solid var(--stage-edge);
    position:relative;
    font-family:"Tinos","Times New Roman",serif;
  }
  .card{
    position:absolute;
    height:302px;
    border-radius:14px;
    overflow:hidden;
    box-shadow:0 2px 6px rgba(0,0,0,.35);
  }
  .front{left:89px;top:39px;width:500px;background:var(--paper)}
  .back-navy{left:606px;top:39px;width:545px;background:radial-gradient(ellipse at 50% 45%,var(--royal),var(--navy) 55%,var(--navy-deep))}
  .back-white{left:89px;top:370px;width:500px;background:var(--paper)}
  .back-green{left:606px;top:370px;width:545px;background:radial-gradient(ellipse at 70% 40%,var(--green-light),var(--green) 55%,var(--green-deep))}

  .house{position:absolute;inset:0}
  .brand{
    position:absolute;left:18px;top:18px;
    display:flex;align-items:center;gap:8px;
    color:var(--navy);font-weight:700;font-size:19px;line-height:1.05;
  }
  .brand-square{width:22px;height:22px;background:var(--green)}
  .headshot{
    position:absolute;left:14px;top:168px;width:104px;height:86px;
    background:linear-gradient(160deg,#9a8f86,#d9c2a6 50%,#6b6560);
    border:2px solid var(--paper);outline:1px solid #888;
  }
  .agent{position:absolute;left:255px;top:108px;width:190px;text-align:center;color:var(--paper)}
  .agent-name{font-size:20px;font-weight:400}
  .agent-title{font-size:11px;margin-top:1px}
  .contact{
    position:absolute;right:14px;top:204px;text-align:right;
    color:var(--paper);font-size:11.5px;line-height:1.45;
  }

  .mark-name{font-weight:700;white-space:nowrap}
  .back-navy .mark-name{position:absolute;left:0;right:0;top:48px;text-align:center;color:var(--paper);font-size:30px}
  .back-navy .offer{position:absolute;left:0;right:0;top:136px;text-align:center;color:var(--paper)}
  .offer-title{font-weight:700;font-size:19px;margin-bottom:6px}
  .back-navy .offer-list{list-style:none;font-size:18px;line-height:1.22}

  .back-white .offer{position:absolute;left:20px;top:42px;color:var(--ink)}
  .back-white .offer-title{color:var(--royal);font-size:18px;margin-bottom:18px}
  .back-white .offer-list{list-style:none;font-size:16.5px;line-height:1.35}
  .back-white .mark-name{position:absolute;right:22px;top:128px;color:var(--navy);font-size:30px}

  .back-green .offer{position:absolute;left:24px;top:42px;color:var(--paper)}
  .back-green .offer-title{font-size:18px;margin-bottom:18px}
  .back-green .offer-list{list-style:none;font-size:16.5px;line-height:1.35}
  .back-green .mark-name{position:absolute;right:26px;top:128px;color:var(--paper);font-size:30px}
</style>
</head>
<body>

<section class="card front">
  <svg class="house" width="500" height="302" viewBox="0 0 500 302" aria-hidden="true">
    <defs>
      <linearGradient id="wall" x1="0" y1="0" x2="1" y2="1">
        <stop offset="0" stop-color="#2a55c4"/>
        <stop offset="0.6" stop-color="#0d2a7a"/>
        <stop offset="1" stop-color="#071a57"/>
      </linearGradient>
    </defs>
    <polygon points="186,302 186,160 366,22 500,118 500,302" fill="url(#wall)"/>
    <polyline points="160,170 366,8 500,104" fill="none" stroke="#4cae3f" stroke-width="6"/>
  </svg>
  <div class="brand"><span class="brand-square"></span><span>Marwick<br>Insurance Solutions</span></div>
  <div class="headshot" role="img" aria-label="Head shot of Lena Marwick"></div>
  <div class="agent">
    <div class="agent-name">Lena Marwick</div>
    <div class="agent-title">Independent Agent</div>
  </div>
  <address class="contact" style="font-style:normal">
    Charlotte, NC<br>
    Phone: 704-555-0142<br>
    Email: Lenamarwick@quillpost.example<br>
    www.marwickInsurance.example
  </address>
</section>

<section class="card back-navy">
  <div class="mark-name">Marwick</div>
  <div class="offer">
    <p class="offer-title">I can also help you with......</p>
    <ul class="offer-list">
      <li>Long-Term Care Insurance | Fixed Annuities</li>
      <li>Life Insurance | Medicare Supplement Insurance</li>
      <li>Individual Major Medical Insurance | Final Expense Insurance</li>
      <li>Medicare Advantage Plans</li>
    </ul>
  </div>
</section>

<section class="card back-white">
  <div class="offer">
    <p class="offer-title">I can also help you with.......</p>
    <ul class="offer-list">
      <li>Long-Term Care Insurance</li>
      <li>Fixed Annuities</li>
      <li>Life Insurance</li>
      <li>Medicare Supplement Insurance</li>
      <li>&nbsp;Individual Major Medical Insurance</li>
      <li>Final Expense Insurance</li>
      <li>Medicare Advantage Plans</li>
    </ul>
  </div>
  <div class="mark-name">Marwick</div>
</section>

<section class="card back-green">
  <div class="offer">
    <p class="offer-title">I can also help you with.......</p>
    <ul class="offer-list">
      <li>Long-Term Care Insurance</li>
      <li>Fixed Annuities</li>
      <li>Life Insurance</li>
      <li>Medicare Supplement Insurance</li>
      <li>&nbsp;Individual Major Medical Insurance</li>
      <li>Final Expense Insurance</li>
      <li>Medicare Advantage Plans</li>
    </ul>
  </div>
  <div class="mark-name">Marwick</div>
</section>

</body>
</html>
```